Patent Law

Need to develop a home page for a patent lawyer.

Colors should go with logo, blues...

Company Name- Corvel Tindry, PLLC

Company Overview-

I am an Intellectual Property Lawyer and focus on patents, copyrights, trademarks, & trade secrets. I work with small businesses and start ups in the chemical and biotech industries.

Why Us-

I am small firm that can provide large-firm service at a reasonable price. I also can charge flat-fees for entreprenuers in certain practice areas.

Services-
Intellectual Property
Patents
Copyrights
Trademarks
Trade secrets
Healthcare Compliance
Elder law
Wills
Trusts

Website we like-
http://www.quarnlowtide.example/ - within industry!!
http://www.vopperhask.example/
http://dulbrickovan.example/
http://thefernwoldguides.example/

Target Market(s)

My customers will be small business, specifically small start-up companies in the chemical and biotech arena.

Industry/Entity Type

Trade

Requirements
Must have
• Colors should go with logo, blues...

```html
<!DOCTYPE html>
<html lang="en">
<head>
<meta charset="utf-8">
<title>Corvel Tindry, PLLC — Patent Law</title>
<link rel="stylesheet" href="https://fonts.googleapis.com/css2?family=Arimo:wght@400;700&family=Play:wght@400;700&display=swap">
<style>
:root{
  --brand-blue:#1f3d8f;
  --brand-blue-dark:#172e6e;
  --ink:#333333;
  --ink-soft:#555555;
  --rule:#d6d6d6;
  --page:#f1f1f1;
  --white:#ffffff;
  --footer:#0b0b0b;
  --footer-text:#c8c8c8;
  --footer-muted:#4a4a4a;
  --steel:#8a9297;
  --field-border:#d9d9d9;
}
*{box-sizing:border-box;margin:0;padding:0}
html,body{width:908px;height:1200px;overflow:hidden}
body{position:relative;background:var(--page);font-family:"Arimo",Arial,sans-serif;color:var(--ink)}
.abs{position:absolute}

/* header */
.top-shade{left:0;top:0;width:908px;height:317px;background:linear-gradient(90deg,#2a2c30 0%,#1a1b1d 60%,#3a3d42 100%)}
.header{left:0;top:0;width:838px;height:97px;background:var(--white);box-shadow:2px 2px 8px rgba(0,0,0,.5)}
.header-accent{left:0;top:0;width:133px;height:4px;background:var(--brand-blue)}
.header-accent-grey{left:133px;top:0;width:705px;height:4px;background:#9aa2a8}
.brand{left:133px;top:28px;display:flex;align-items:center;gap:8px}
.brand-mark{width:18px;height:18px;border-radius:50%;background:var(--brand-blue)}
.brand-name{font-size:13px;color:#2a3a6a;font-weight:400;letter-spacing:.5px}
.contact-line{left:627px;font-size:11px;color:#333;display:flex;align-items:center;gap:8px}

/* nav */
.nav{left:0;top:97px;width:838px;height:33px}
.nav-menu{display:flex;list-style:none;height:33px;position:absolute;left:120px;top:0}
.nav-menu li{font-size:10px;color:var(--white);line-height:33px;padding:0 15px;border-right:1px solid rgba(255,255,255,.35)}
.nav-menu li:last-child{border-right:none}

/* hero */
.hero-photo{left:0;top:130px;width:908px;height:187px;background:radial-gradient(ellipse at 30% 60%,#e8b866 0%,#a46a1e 30%,#5a3812 60%,#2b1b0a 100%)}
.hero-title-band{left:0;top:164px;width:465px;height:32px;background:linear-gradient(90deg,rgba(255,255,255,.55),rgba(255,255,255,.85))}
.hero-title{left:136px;top:169px;font-family:"Play",Arial,sans-serif;font-weight:700;font-size:19px;color:#1a1a1a;letter-spacing:.3px}
.hero-copy{left:136px;top:203px;width:380px;font-size:9px;line-height:16.5px;color:var(--white)}
.hero-more{left:136px;top:272px;width:63px;height:17px;border:1px solid var(--white);font-size:9px;color:var(--white);line-height:15px;text-align:center}
.slider-strip{left:660px;top:130px;width:248px;height:187px}
.slider-num{font-size:9px;color:var(--white)}

/* content */
.content{left:0;top:317px;width:908px;height:396px;background:linear-gradient(#ececec,#ffffff)}
.col-divider{width:1px;background:var(--rule);top:342px;height:350px}
.section-title{display:flex;align-items:center;gap:7px;font-family:"Play",Arial,sans-serif;font-weight:700;font-size:11.5px;color:var(--brand-blue)}
.section-title::before{content:"";width:12px;height:12px;border-radius:50%;background:var(--brand-blue)}
.team-photo{left:136px;top:379px;width:185px;height:60px;background:linear-gradient(90deg,#6d7a8c,#c9c2b6 40%,#8a8f99 70%,#dcdcdc)}
.why-copy{left:136px;width:185px;font-size:9px;line-height:16.7px;color:var(--ink-soft);text-align:justify}
.read-more{left:136px;top:660px;font-size:9px;color:var(--ink)}
.services{left:360px;top:382px;width:176px;list-style:none}
.services li{height:26px;line-height:26px;font-size:10px;color:var(--ink-soft);padding-left:13px;position:relative;border-bottom:1px dashed #e0e0e0}
.services li::before{content:"";position:absolute;left:4px;top:9px;width:3px;height:8px;background:var(--brand-blue)}
.services li.active{background:#d9d9d9;border-bottom-color:#d9d9d9}
.field{left:587px;width:185px;height:24px;border:1px solid var(--field-border);background:var(--white);font-size:7px;color:#999;padding:7px 5px}
.field-select::after{content:"";position:absolute;right:0;top:0;width:12px;height:22px;background:var(--steel)}
.form-note{left:590px;top:659px;font-size:7px;color:#444}
.subscribe{left:692px;top:676px;width:80px;height:23px;background:linear-gradient(#3b3b3b,#1c1c1c);color:var(--white);font-size:9px;font-weight:700;text-align:center;line-height:23px}

/* footer */
.footer{left:0;top:713px;width:908px;height:487px;background:linear-gradient(#141414,var(--footer))}
.footer-title{top:741px;font-family:"Play",Arial,sans-serif;font-weight:700;font-size:12px;color:var(--white);letter-spacing:.5px}
.footer-divider{width:1px;top:741px;height:230px;background:#262626}
.footer-links{left:136px;top:782px;list-style:none}
.footer-links li{font-size:9px;color:var(--footer-text);height:28px}
.news-date{left:235px;font-size:10px;color:var(--footer-text)}
.news-age{left:235px;font-size:6px;color:var(--footer-muted)}
.news-copy{left:235px;width:160px;font-size:8.5px;line-height:14.5px;color:var(--footer-muted);text-align:justify}
.social-row{left:439px;display:flex;align-items:center;gap:10px}
.social-dot{width:25px;height:25px;border-radius:50%;background:#bdbdbd}
.social-label{font-size:8.5px;color:var(--footer-text)}
.map{left:568px;top:788px;width:204px;height:124px;background:linear-gradient(135deg,#e9e4d8,#d8d4ca 60%,#c9c7c2)}
.footer-rule{left:136px;top:1007px;width:636px;height:1px;background:#2e2e2e}
.footer-brand{left:0;width:908px;top:1040px;display:flex;justify-content:center;align-items:center;gap:10px}
.footer-brand .brand-mark{background:#6f6f6f;width:22px;height:22px}
.footer-brand-name{font-size:16px;color:#7a7a7a;letter-spacing:.5px}
.copyright{left:0;width:908px;top:1131px;text-align:center;font-size:7px;color:#8a8a8a}
</style>
</head>
<body>

<div class="abs top-shade"></div>

<header>
  <div class="abs header">
    <div class="abs header-accent"></div>
    <div class="abs header-accent-grey"></div>
    <div class="abs brand"><span class="brand-mark"></span><span class="brand-name">Corvel Tindry, PLLC</span></div>
    <div class="abs contact-line" style="top:35px">
      <svg width="11" height="8" viewBox="0 0 11 8"><rect x=".5" y=".5" width="10" height="7" fill="#1c2a4a" stroke="#1c2a4a"/><path d="M.5 .5 5.5 4.5 10.5 .5" fill="none" stroke="#fff" stroke-width="1"/></svg>
      info@corveltindry.example
    </div>
    <div class="abs contact-line" style="top:54px">
      <svg width="11" height="12" viewBox="0 0 8 12"><rect x="1" y=".5" width="6" height="11" rx="1" fill="none" stroke="#1c2a4a" stroke-width="1.4"/><rect x="3" y="9" width="2" height="1" fill="#1c2a4a"/></svg>
      555|010|482
    </div>
  </div>

  <nav class="abs nav">
    <svg class="abs" style="left:0;top:0" width="838" height="33" viewBox="0 0 838 33">
      <polygon points="0,0 660,0 674,33 0,33" fill="#1f3d8f"/>
      <polygon points="660,0 838,0 838,33 674,33" fill="#8f989e"/>
      <line x1="0" y1="0.5" x2="838" y2="0.5" stroke="#3b5bb0"/>
    </svg>
    <ul class="nav-menu">
      <li>Home</li><li>About Us</li><li>Principals</li><li>Blog</li><li>News</li><li>Contact Us</li>
    </ul>
  </nav>
</header>

<section class="hero">
  <div class="abs hero-photo" role="img" aria-label="Hero photograph: a professional woman in glasses in a warmly lit office"></div>
  <svg class="abs slider-strip" width="248" height="187" viewBox="0 0 248 187">
    <polygon points="0,0 40,0 88,187 48,187" fill="rgba(0,0,0,.35)"/>
    <polygon points="16,0 40,0 52,24 28,24" fill="#1f3d8f"/>
    <polygon points="60,143 88,143 96,165 66,165" fill="rgba(255,255,255,.18)"/>
    <path d="M81 150 77 154 81 158" fill="none" stroke="#fff" stroke-width="2"/>
    <path d="M88 172 92 176 88 180" fill="none" stroke="#fff" stroke-width="2"/>
  </svg>
  <div class="abs slider-num" style="left:691px;top:142px">1</div>
  <div class="abs slider-num" style="left:701px;top:168px">2</div>
  <div class="abs slider-num" style="left:711px;top:194px">3</div>
  <div class="abs slider-num" style="left:719px;top:219px">4</div>
  <div class="abs slider-num" style="left:727px;top:244px">5</div>
  <div class="abs hero-title-band"></div>
  <h1 class="abs hero-title">WE PROVIDE YOU BETTER SOLUTION</h1>
  <p class="abs hero-copy">Lorem Ipsum is simply dummy text of the printing and typesetting industry. Lorem Ipsum has been the industry's standard dummy text ever since the scrembled it to make a type specimen book the industry's standard dummy text ever since the scrembled it to make a type specimen book.</p>
  <div class="abs hero-more">Read more »</div>
</section>

<main>
  <div class="abs content"></div>
  <div class="abs col-divider" style="left:340px"></div>
  <div class="abs col-divider" style="left:568px"></div>

  <h2 class="abs section-title" style="left:136px;top:352px">WHY US</h2>
  <div class="abs team-photo" role="img" aria-label="Team photograph of the firm's four attorneys"></div>
  <p class="abs why-copy" style="top:448px">Lorem Ipsum is simply dummy text of the printing and typesetting industry. Lorem Ipsum has been the industry's standard dummy text ever since the scrembled it to make a type specimen book.</p>
  <p class="abs why-copy" style="top:527px">Lorem Ipsum has been the industry's standard dummy text ever since the scrembled it to make a type specimen book. Lorem Ipsum has been the industry's standard dummy text ever. Lorem Ipsum has been the industry's standard dummy text ever. Lorem Ipsum has been the industry's standard dummy text ever.</p>
  <div class="abs read-more">▸▸ read more</div>

  <h2 class="abs section-title" style="left:360px;top:352px">OUR SERVICES</h2>
  <ul class="abs services">
    <li>Intellectual Property</li><li>Patents</li><li class="active">Copyrights</li><li>Trademarks</li><li>Trade secrets</li><li>Healthcare Compliance</li><li>Elder law</li><li>Wills</li><li>Trusts</li>
  </ul>

  <h2 class="abs section-title" style="left:587px;top:352px">CONTACT INFO</h2>
  <div class="abs field" style="top:380px">Name:</div>
  <div class="abs field" style="top:416px">Email:</div>
  <div class="abs field" style="top:451px">Phone:</div>
  <div class="abs field field-select" style="top:487px">Type Of Case:</div>
  <div class="abs field" style="top:523px">Where:</div>
  <div class="abs field" style="top:561px;height:90px">Comments:</div>
  <div class="abs form-note">*All fields are mandatory</div>
  <div class="abs subscribe">SUBSCRIBE</div>
</main>

<footer>
  <div class="abs footer"></div>
  <div class="abs footer-divider" style="left:209px"></div>
  <div class="abs footer-divider" style="left:413px"></div>
  <div class="abs footer-divider" style="left:544px"></div>

  <h3 class="abs footer-title" style="left:136px">LINKS</h3>
  <ul class="abs footer-links">
    <li>Home</li><li>About Us</li><li>Principals</li><li>Blog</li><li>News</li><li>Contact Us</li>
  </ul>

  <h3 class="abs footer-title" style="left:235px">NEWS</h3>
  <div class="abs news-date" style="top:783px">- 12 Jan 2014</div>
  <div class="abs news-age" style="top:797px">posted 6 min ago</div>
  <p class="abs news-copy" style="top:806px">Lorem Ipsum has been the industry's standard dummy text ever. Lorem Ipsum has been the industry's standard dummy text ever.</p>
  <div class="abs news-date" style="top:880px">- 12 Jan 2014</div>
  <div class="abs news-age" style="top:894px">posted 6 min ago</div>
  <p class="abs news-copy" style="top:903px">Lorem Ipsum has been the industry's standard dummy text ever. Lorem Ipsum has been the industry's standard dummy text ever.</p>

  <h3 class="abs footer-title" style="left:439px">GET SOCIAL</h3>
  <div class="abs social-row" style="top:777px"><span class="social-dot"></span><span class="social-label">CIRCLEPAGE</span></div>
  <div class="abs social-row" style="top:810px"><span class="social-dot"></span><span class="social-label">CHIRPLINE</span></div>
  <div class="abs social-row" style="top:842px"><span class="social-dot"></span><span class="social-label">SEARCHPLUS</span></div>
  <div class="abs social-row" style="top:875px"><span class="social-dot"></span><span class="social-label">WORKLINK</span></div>

  <h3 class="abs footer-title" style="left:565px">VIEW MAP</h3>
  <div class="abs map" role="img" aria-label="Street map showing the office location"></div>

  <div class="abs footer-rule"></div>
  <div class="abs footer-brand"><span class="brand-mark"></span><span class="footer-brand-name">Corvel Tindry, PLLC</span></div>
  <div class="abs copyright">© 2013 Corvel Tindry, PLLC &nbsp;&nbsp;|&nbsp;&nbsp; Privacy Policy</div>
</footer>

</body>
</html>
```